Asia based real estate financing firm needs and AWESOME design for a biz card -Harbor Lending Circle

Looking for a stylish, & corporate-looking business card for a real estate financing brokerage firm in Asia, offering global mortgage loans. I uploaded our current logos. We would like to add a splash of color (perhaps the house icon) or any other suggestions are open. For the winning designer, we have a lot of work! Thanks and best of luck!

Target Market(s)

Real estate investors globally. We want to look more like a BANK and NOT a real estate company. Please don't play up on a "house" design.

Industry/Entity Type

Banking

Contact Information for Business Card

Harbor Lending Circle
Peter Wilks
Co-Founder | Partner

14 Cassia Lane, Suite 310
Singapore 047219
www.hlc-example.asia
peterwilks@hlc-example.asia
+65 555-0142
WeChat: peterwilks

Colors

Designer to choose colors to be used in the design.

Requirements
Must have
• Must have the standard business requirements for a card; name, address, email, etc
• Can be horizontal or vertical.
Nice to have
• It would be great to see some sort of variation to the logo with a pop of color. Red is good as we're in Asia, however, other options work as well.
• Our tag line is - Boundless Lending. It doesn't have to be on the card but might be nice.
• I'd like to start seeing our tagline within the cards as well. - Boundless Lending.
• Also, please add our location. The location for this card is Singapore so perhaps it can be highlighted or emphasised in some way.
• Singapore | Hong Kong | Shanghai | Manila
• As we will soon open an office in Shanghai, having an option for both languages would be great.
Should not have
• I'm exceited and open to your creativity ... knock it out of the park!

```html
<!DOCTYPE html>
<html lang="en">
<head>
<meta charset="utf-8">
<title>Harbor Lending Circle – Business Card</title>
<link rel="stylesheet" href="https://fonts.googleapis.com/css2?family=Cormorant+Garamond:wght@600&family=Montserrat:wght@400;600&display=swap">
<style>
  :root {
    --backdrop: #e4e4e4;
    --paper: #ececeb;
    --ink: #141414;
    --night: #111111;
    --accent: #b01e22;
    --muted: #6e6e6e;
    --snow: #ededed;
  }
  * { margin: 0; padding: 0; box-sizing: border-box; }
  html, body { width: 1200px; height: 1200px; overflow: hidden; background: var(--backdrop); }
  body { position: relative; font-family: "Montserrat", sans-serif; }

  .card { position: absolute; left: 227px; width: 745px; height: 424px; }
  .card--front { top: 136px; background: var(--paper); }
  .card--back { top: 639px; background: var(--night); }

  .rule { position: absolute; left: 45px; top: 0; width: 2px; height: 100%; background: var(--accent); }

  .brand { position: absolute; display: flex; align-items: center; gap: 12px;
    font-family: "Cormorant Garamond", serif; font-weight: 600; white-space: nowrap; }
  .brand__mark { width: 12px; height: 12px; background: var(--accent); flex: none; }
  .card--front .brand { left: 73px; top: 92px; font-size: 40px; color: var(--ink); }

  .person { position: absolute; left: 73px; top: 230px; }
  .person__name { font-weight: 600; font-size: 22px; color: var(--accent); line-height: 1.2; }
  .person__role { font-size: 16.5px; color: var(--muted); margin-top: 3px; }

  .icon { position: absolute; left: 36px; width: 20px; height: 20px; }

  .contacts { position: absolute; left: 73px; top: 314px; list-style: none;
    font-size: 16.5px; color: var(--muted); line-height: 24px; }
  .address { position: absolute; right: 35px; top: 338px; text-align: right;
    font-size: 16.5px; color: var(--muted); line-height: 24px; font-style: normal; }

  .card--back .brand { left: 0; right: 0; top: 178px; justify-content: center;
    font-size: 46px; color: var(--snow); }
  .tagline { position: absolute; left: 0; right: 0; top: 294px; text-align: center;
    font-size: 13px; letter-spacing: 0.55em; color: var(--snow); padding-left: 0.55em; }
</style>
</head>
<body>

<section class="card card--front" aria-label="Card front">
  <div class="rule"></div>

  <div class="brand"><span class="brand__mark"></span>Harbor Lending Circle</div>

  <svg class="icon" style="top:246px" viewBox="0 0 20 20" aria-hidden="true">
    <circle cx="10" cy="10" r="10" fill="var(--accent)"/>
    <circle cx="10" cy="7.5" r="3" fill="var(--paper)"/>
    <path d="M4.5 15.5c1-3 3-4 5.5-4s4.5 1 5.5 4z" fill="var(--paper)"/>
  </svg>
  <div class="person">
    <div class="person__name">Peter Wilks</div>
    <div class="person__role">Co-Founder | Partner</div>
  </div>

  <svg class="icon" style="top:316px" viewBox="0 0 20 20" aria-hidden="true">
    <circle cx="10" cy="10" r="10" fill="var(--accent)"/>
    <rect x="6.5" y="4" width="7" height="12" rx="1.5" fill="none" stroke="var(--paper)" stroke-width="1.4"/>
  </svg>
  <svg class="icon" style="top:340px" viewBox="0 0 20 20" aria-hidden="true">
    <circle cx="10" cy="10" r="10" fill="var(--accent)"/>
    <rect x="4.5" y="6" width="11" height="8" fill="none" stroke="var(--paper)" stroke-width="1.3"/>
    <path d="M4.5 6l5.5 4.5 5.5-4.5" fill="none" stroke="var(--paper)" stroke-width="1.3"/>
  </svg>
  <svg class="icon" style="top:364px" viewBox="0 0 20 20" aria-hidden="true">
    <circle cx="10" cy="10" r="10" fill="var(--accent)"/>
    <circle cx="10" cy="10" r="5.5" fill="none" stroke="var(--paper)" stroke-width="1.3"/>
    <path d="M4.5 10h11M10 4.5c-2.5 3-2.5 8 0 11M10 4.5c2.5 3 2.5 8 0 11" fill="none" stroke="var(--paper)" stroke-width="1"/>
  </svg>

  <ul class="contacts">
    <li>+65 555-0142</li>
    <li>peterwilks@hlc-example.asia</li>
    <li>www.hlc-example.asia</li>
  </ul>

  <address class="address">
    14 Cassia Lane, Suite 310<br>
    Singapore 047219
  </address>
</section>

<section class="card card--back" aria-label="Card back">
  <div class="brand"><span class="brand__mark"></span>Harbor Lending Circle</div>
  <p class="tagline">BOUNDLESS&nbsp;&nbsp;LENDING</p>
</section>

</body>
</html>
```